Cool payments solutions startup needs a brochure and product overview (Tal'vo)

We are a technology company that is working a platform to improve social inclusion in Latin America. Name Talvo means "work done for the good of the community" and we are targeting financial institutions and young profesionals (think osprey or blue lynx).

We need a brochure that would provide a brief overview of our platform and our services.

We prepared the illustration design that would describe the brochure, the rest is up to the designer to provide ideas.

We are a financial company focusing on financial inclusion.

Idea is to have a simple, minimalistic design. You can use sketch or handwriting to assist int he design.

Enclosed is the provided outline of the brochure with our sketched. It is necessary to provide illustrations from the sketched that are provided in the brochure.

Please keep in mind we don't have the final text (use generic text) and that we will translate all the text to several languages.

Main focus is digital distribution, not planning print for now. In case you will prepare print prep it will be two A4 pages (A5).

Ideas for design:
www.quorvane.org
http://plinketa.com
http://mervadolix.io

Target Market(s)

technology companies and developers

Industry/Entity Type

Information Technology

Font styles to use
Serif
Sans Serif

Colors
00a990
33b8a4
88d0c7
9bcb3c
abd037
cadf82
eaf2ce
f8fcfc

Requirements
Must have
• Illustration as sketched in the attached documents.
• We are open for suggestions, but the basic elements must be matched.
Nice to have
• A complete 4 pages for a print (A4).
• We will distribute the brochure digitally.

```html
<!DOCTYPE html>
<html lang="en">
<head>
<meta charset="utf-8">
<title>Tal'vo – Print Format</title>
<link rel="stylesheet" href="https://fonts.googleapis.com/css2?family=Montserrat:wght@300;400;600&display=swap">
<style>
  :root{
    --teal:#00a990;
    --teal-mid:#33b8a4;
    --teal-soft:#88d0c7;
    --green:#9bcb3c;
    --green-2:#abd037;
    --green-soft:#cadf82;
    --green-pale:#eaf2ce;
    --paper:#ffffff;
    --bg:#e9e9e9;
    --ink:#444;
    --muted:#888;
  }
  *{box-sizing:border-box;margin:0;padding:0}
  html,body{width:901px;height:1200px;overflow:hidden}
  body{background:var(--bg);font-family:"Montserrat",sans-serif;color:var(--ink);position:relative}
  .page-title{position:absolute;top:36px;left:0;width:100%;text-align:center;font-size:22px;font-weight:400;color:#111;letter-spacing:.5px}
  .spread{position:absolute;left:80px;width:740px;height:523px;display:flex;background:var(--paper);box-shadow:0 14px 30px rgba(0,0,0,.18)}
  .spread--outer{top:90px}
  .spread--inner{top:650px;border-bottom:5px solid var(--teal)}
  .page{position:relative;width:370px;height:100%;overflow:hidden}
  .page + .page{border-left:1px solid #e4e4e4}

  /* back page */
  .back__band{position:absolute;left:0;top:100px;width:100%;height:330px;background:linear-gradient(160deg,var(--teal) 0%,var(--teal-mid) 100%);color:#fff;padding:60px 0 0 110px}
  .brand-name{font-weight:300;font-size:46px;line-height:1;letter-spacing:1px}
  .brand-tag{font-weight:300;font-size:11px;margin-top:6px}
  .contact{margin-top:30px;font-weight:300;font-size:10.5px;line-height:1.6}
  .contact__head{font-size:13px;margin-bottom:4px}
  .contact p + p{margin-top:8px}

  /* cover */
  .cover__brand{position:absolute;top:28px;left:0;width:100%;text-align:center;color:var(--teal)}
  .cover__brand .brand-name{font-size:44px}
  .cover__art{position:absolute;left:0;top:110px;width:100%;height:300px;background:radial-gradient(circle at 50% 50%,var(--teal-soft) 0%,var(--teal-mid) 35%,var(--teal) 75%)}
  .cover__motto{position:absolute;bottom:52px;width:100%;text-align:center;color:var(--teal);font-weight:300;font-size:11.5px;letter-spacing:.3px}

  /* inner left */
  .intro{padding:42px 24px 0}
  .intro__title{color:var(--teal);font-weight:400;font-size:17px;line-height:1.2;text-align:center}
  .intro__sub{font-size:8px;color:var(--ink);margin-top:8px;padding-left:4px}
  .flow{display:block;margin:10px auto 0}
  .intro__body{font-size:7px;color:var(--muted);text-align:center;line-height:1.5;margin-top:44px;padding:0 12px}

  /* inner right */
  .features{list-style:none;padding:24px 26px 0 24px}
  .feature{display:flex;align-items:center;gap:14px;height:67px;border-bottom:1px solid #ddd}
  .feature:last-child{border-bottom:none}
  .feature__icon{flex:0 0 26px;height:26px}
  .feature__name{color:var(--teal);font-size:9px;font-weight:600;letter-spacing:.5px}
  .feature__text{font-size:6.5px;color:var(--muted);line-height:1.45;margin-top:2px}
  .flow text{font-family:"Montserrat",sans-serif;fill:#fff;font-size:6.5px}
</style>
</head>
<body>
  <h1 class="page-title">PRINT FORMAT</h1>

  <section class="spread spread--outer">
    <div class="page back">
      <div class="back__band">
        <div class="brand-name">Tal'vo</div>
        <div class="brand-tag">Public infrastructure for money</div>
        <div class="contact">
          <div class="contact__head">Contact</div>
          <p>418 Calloway Lane Northeast<br>Harwell, DC 20099</p>
          <p>(555) 014-2290</p>
          <p>info@talvo.com</p>
          <p>www.talvo.com</p>
        </div>
      </div>
    </div>
    <div class="page cover">
      <div class="cover__brand">
        <div class="brand-name">Tal'vo</div>
        <div class="brand-tag">Public infrastructure for money</div>
      </div>
      <div class="cover__art" role="img" aria-label="Illustration: many white hands reaching toward the centre from all sides on a teal field"></div>
      <p class="cover__motto">Tal'vo – work for the good of the community.</p>
    </div>
  </section>

  <section class="spread spread--inner">
    <div class="page intro">
      <h2 class="intro__title">Money is only information about<br>what we owe each other.</h2>
      <p class="intro__sub">2.5 billion people accross the world don't have access to financial services.</p>
      <svg class="flow" width="322" height="260" viewBox="0 0 322 260" aria-label="Flow: people, channels, transactions and institutions">
        <rect x="0" y="0" width="322" height="52" fill="#abd037"/>
        <rect x="0" y="52" width="322" height="52" fill="#00a990"/>
        <rect x="0" y="104" width="322" height="52" fill="#9bcb3c"/>
        <rect x="0" y="156" width="322" height="52" fill="#33b8a4"/>
        <rect x="0" y="208" width="322" height="52" fill="#9bcb3c"/>
        <polygon points="153,52 169,52 161,60" fill="#abd037"/>
        <polygon points="153,104 169,104 161,112" fill="#00a990"/>
        <polygon points="153,156 169,156 161,164" fill="#9bcb3c"/>
        <polygon points="153,208 169,208 161,216" fill="#33b8a4"/>
        <g fill="#fff">
          <circle cx="42" cy="18" r="6"/><rect x="34" y="25" width="16" height="9" rx="4"/>
          <rect x="104" y="14" width="18" height="18"/>
          <rect x="176" y="12" width="14" height="22"/>
          <rect x="242" y="14" width="20" height="14"/>
          <rect x="100" y="66" width="22" height="16" rx="2"/>
          <rect x="206" y="66" width="22" height="18" rx="2"/>
          <rect x="60" y="120" width="18" height="12"/>
          <circle cx="120" cy="126" r="9"/>
          <polygon points="210,119 222,114 222,136 210,131"/>
          <rect x="266" y="116" width="10" height="18" rx="2"/>
          <circle cx="118" cy="176" r="4"/><circle cx="108" cy="170" r="3"/><circle cx="128" cy="170" r="3"/><circle cx="108" cy="183" r="3"/><circle cx="128" cy="183" r="3"/>
          <circle cx="228" cy="176" r="8"/><circle cx="220" cy="180" r="6"/><circle cx="236" cy="180" r="6"/>
          <rect x="28" y="222" width="16" height="14"/>
          <rect x="82" y="222" width="20" height="14"/>
          <ellipse cx="140" cy="230" rx="9" ry="6"/>
          <rect x="186" y="224" width="20" height="10" rx="5"/>
          <rect x="234" y="222" width="20" height="14" rx="2"/>
          <rect x="282" y="220" width="10" height="18" rx="2"/>
        </g>
        <text x="32" y="45">Person</text><text x="104" y="45">Store</text><text x="168" y="45">Company</text><text x="238" y="45">Web App</text>
        <text x="100" y="96">Wallet</text><text x="148" y="80">Pay/Receive</text><text x="206" y="96">Cashier</text>
        <text x="60" y="146">SMS</text><text x="116" y="146">Web</text><text x="148" y="128">Using any</text><text x="150" y="136">Channels</text><text x="210" y="146">Voice</text><text x="264" y="146">App</text>
        <text x="100" y="199">Transaction</text><text x="148" y="176">From any</text><text x="148" y="184">Currency</text><text x="146" y="192">or gateway</text><text x="216" y="199">Gateway</text>
        <text x="22" y="251">Agents</text><text x="82" y="251">Banks</text><text x="128" y="251">Loyalty</text><text x="176" y="251">Credit Unions</text><text x="230" y="251">Credit Card</text><text x="272" y="251">Mobile Money</text>
      </svg>
      <p class="intro__body">Lorem ipsum dolor sit amet, consectetuer adipiscing elit, sed diam nonummy nibh euismod tincidunt ut laoreet dolore magna aliquam erat volutpat. Ut wisi enim ad minim veniam, quis nostrud exerci tation ullamcorper suscipit lobortis nisl ut aliquip ex ea commodo consequat.</p>
    </div>

    <div class="page">
      <ul class="features">
        <li class="feature">
          <svg class="feature__icon" viewBox="0 0 26 26"><rect x="3" y="7" width="20" height="14" rx="2" fill="#00a990"/><rect x="15" y="11" width="8" height="6" fill="#33b8a4"/></svg>
          <div><div class="feature__name">WALLET</div><p class="feature__text">Universal, omni-channel wallet that is accessible on any device. True one action payment making it as simple and accessible as cash.</p></div>
        </li>
        <li class="feature">
          <svg class="feature__icon" viewBox="0 0 26 26"><rect x="3" y="12" width="20" height="10" fill="#00a990"/><rect x="7" y="5" width="10" height="7" fill="#00a990"/></svg>
          <div><div class="feature__name">CASHIER</div><p class="feature__text">Universal interface for accepting any form payments. Personalized information and benefits program provide a contexts to what otherwise would be only a simple receipt.</p></div>
        </li>
        <li class="feature">
          <svg class="feature__icon" viewBox="0 0 26 26"><polygon points="4,10 18,4 18,22 4,16" fill="#00a990"/><rect x="7" y="16" width="4" height="7" fill="#00a990"/></svg>
          <div><div class="feature__name">CHANNEL</div><p class="feature__text">Text message, voice call, ussd, web or app. Any channel you prefer to use. Powered by Relaynet – 4 billion transactions per month, 190 countries, 800+ operators.</p></div>
        </li>
        <li class="feature">
          <svg class="feature__icon" viewBox="0 0 26 26"><circle cx="13" cy="12" r="7" fill="#00a990"/><circle cx="7" cy="15" r="5" fill="#00a990"/><circle cx="19" cy="15" r="5" fill="#00a990"/><rect x="7" y="15" width="12" height="5" fill="#00a990"/></svg>
          <div><div class="feature__name">GATEWAYS</div><p class="feature__text">Gateways are issuing entities that people trust to hold their deposit and issue credits into the network. Tal'vo network connects the different gateways.</p></div>
        </li>
        <li class="feature">
          <svg class="feature__icon" viewBox="0 0 26 26" fill="#00a990"><circle cx="13" cy="13" r="4"/><circle cx="5" cy="8" r="3"/><circle cx="21" cy="8" r="3"/><circle cx="5" cy="18" r="3"/><circle cx="21" cy="18" r="3"/><circle cx="13" cy="3" r="2.5"/><circle cx="13" cy="23" r="2.5"/></svg>
          <div><div class="feature__name">TRANSACTIONS</div><p class="feature__text">Tal'vo uses a global ledger to keep track of all the balances and transactions for every single account on the network. Tal'vo ensures that all transactions are valid and get applied.</p></div>
        </li>
        <li class="feature">
          <svg class="feature__icon" viewBox="0 0 26 26" fill="#00a990"><ellipse cx="12" cy="20" rx="8" ry="3.5"/><ellipse cx="12" cy="14" rx="8" ry="3.5"/><ellipse cx="14" cy="8" rx="8" ry="3.5"/></svg>
          <div><div class="feature__name">CURRENCY</div><p class="feature__text">Tal'vo can allow to send any currency between any address in the system trough its built-in exchange. Pesas is the universal bridge currency used to settle dollars, yens, pesos, loyalty points, giftcards or bitcoins.</p></div>
        </li>
        <li class="feature">
          <svg class="feature__icon" viewBox="0 0 26 26"><path d="M13 2 L22 6 V13 C22 19 18 22 13 24 C8 22 4 19 4 13 V6 Z" fill="#00a990"/><path d="M9 13 L12 16 L17 10" stroke="#fff" stroke-width="2" fill="none"/></svg>
          <div><div class="feature__name">ADDRESS</div><p class="feature__text">Each unique Tal'vo address can be referenced by something we all know – your phone number. Two factor authentication and global ledger ensure a secure, fraud free system.</p></div>
        </li>
      </ul>
    </div>
  </section>
</body>
</html>
```